create a webpage for optometry practice

I'm looking to create a professional and elegant webpage for my practice. I prefer neutral earthy colors, but I am open to other ideas. I have included an image of my logo to be used in the process. This will be a page that will illustrate information about my practice and the kind of services we offer. I am in process of having the practice remodeled. So I don't have any photos of my practice to include yet.

Target Market(s)

My practice serves young and mature families.

Industry/Entity Type

It Professional

Number of Pages Required

5+ page

Font styles to use
Sans Serif

Colors
33a6d7
86cfc6
85cae6
cadf82
3276b5
faa54b
abd036
f78c1e

Requirements
Must have
• I would need to incorporate information about my practice, services, insurance accepted, make appointment, contact us, and about our family.
Nice to have
• I would like to see something fresh, modern, and unique

```html
<!DOCTYPE html>
<html lang="en">
<head>
<meta charset="utf-8">
<title>Lumina Eye Care</title>
<link href="https://fonts.googleapis.com/css2?family=Raleway:wght@400;500;600;700&display=swap" rel="stylesheet">
<style>
:root{
  --sky:#85cae6;
  --blue:#33a6d7;
  --navy:#3276b5;
  --teal:#86cfc6;
  --orange:#f78c1e;
  --orange-soft:#faa54b;
  --lime:#abd036;
  --lime-soft:#cadf82;
  --ink:#555;
  --dark:#333;
  --white:#fff;
}
*{margin:0;padding:0;box-sizing:border-box}
html,body{width:919px;height:1200px;overflow:hidden}
body{background:var(--sky);font-family:'Raleway',sans-serif;color:var(--ink);position:relative}
.page{position:absolute;left:90px;top:30px;width:741px;height:1092px;background:var(--white)}
.abs{position:absolute}
.brand{left:24px;top:18px;display:flex;align-items:center;gap:6px;font-size:15px;font-weight:500;color:var(--dark);letter-spacing:.5px}
.brand .dot{width:12px;height:12px;border-radius:50%;background:var(--orange)}
.nav{right:22px;top:28px;display:flex;gap:30px;font-size:9.5px;font-weight:500;color:var(--dark)}
.nav .active{color:var(--orange)}
.hero{left:9px;top:66px;width:721px;height:384px;background:linear-gradient(100deg,#e9c7a2 0%,#f2efe9 35%,#dcdde0 55%,#c9a08c 75%,#7a3f8e 100%)}
.arrow{top:158px}
.caption{left:0;bottom:0;width:721px;height:66px;background:rgba(30,30,30,.82)}
.caption p{position:absolute;left:19px;top:23px;width:470px;font-size:10px;line-height:14px;color:#eee}
.btn-appt{position:absolute;left:539px;top:21px;width:165px;height:30px;background:var(--lime);color:var(--white);font-size:11px;font-weight:700;display:flex;align-items:center;justify-content:center}
h2{font-weight:700;color:var(--navy);font-size:20px}
.text{font-size:8.8px;line-height:15.2px;color:var(--ink)}
.welcome{left:7px;top:490px;width:475px}
.welcome h2{margin-bottom:16px}
.welcome .text+.text{margin-top:15px}
.services{left:503px;top:476px;width:228px;height:230px;background:var(--orange);border-radius:3px;padding:17px 19px}
.services h3{color:var(--white);font-size:19px;font-weight:700;margin-bottom:17px}
.services li{list-style:none;color:var(--white);font-size:11.5px;height:22.9px;display:flex;align-items:center;gap:14px}
.services li svg{flex:none}
.news{left:8px;top:757px;width:229px}
.about{left:255px;top:757px;width:229px}
.col h2{font-size:19px;padding-bottom:8px;border-bottom:1px solid #ccc}
.post{display:flex;gap:11px;margin-top:12px;align-items:center}
.date{width:60px;height:60px;border-radius:50%;background:var(--teal);color:var(--white);font-size:8.5px;font-weight:700;display:flex;align-items:center;justify-content:center;text-align:center;line-height:11px;flex:none}
.post-title{font-size:9px;font-weight:700;line-height:15px;color:var(--dark)}
.post-body{margin-top:7px;padding-bottom:10px}
.news .divider{border-top:1px solid #ccc;margin-top:2px}
.about-photo{width:230px;height:136px;margin-top:9px;background:linear-gradient(135deg,#cfe6f3,#eef4f7 55%,#dfe9ef)}
.about .text{margin-top:12px}
.appt{left:503px;top:745px;width:228px;height:318px;background:var(--lime);border-radius:3px;padding:14px 11px}
.appt h3{color:var(--white);font-size:19px;font-weight:700;line-height:23px;margin-left:2px;margin-bottom:6px}
.field{width:209px;height:25px;background:var(--lime-soft);color:var(--white);font-size:8.5px;padding:8px 5px;margin-bottom:16px}
.field.msg{height:70px;margin-top:-16px;position:relative;top:1px}
.submit{width:82px;height:25px;background:var(--blue);color:var(--white);font-size:11px;font-weight:700;display:flex;align-items:center;justify-content:center;margin-top:-1px}
.footer-nav{left:89px;top:1138px;display:flex;gap:16px;font-size:9.5px;color:var(--white)}
.copy{left:89px;top:1164px;font-size:9px;color:var(--white)}
.social{left:803px;top:1147px;display:flex;gap:8px}
.social span{width:10px;height:10px;border-radius:50%;background:var(--white)}
</style>
</head>
<body>
<div class="page">
  <div class="abs brand"><span class="dot"></span>LUMINA EYE</div>
  <nav class="abs nav">
    <span class="active">Home</span><span>About Practise</span><span>Services</span><span>Insurance</span><span>Appointment</span><span>Our family</span><span>Contact Us</span>
  </nav>

  <section class="abs hero" role="img" aria-label="Photo of a patient having an eye examination at a slit lamp">
    <svg class="abs arrow" style="left:25px" width="18" height="30" viewBox="0 0 18 30"><path d="M15 3 L4 15 L15 27" fill="none" stroke="var(--blue)" stroke-width="4"/></svg>
    <svg class="abs arrow" style="left:680px" width="18" height="30" viewBox="0 0 18 30"><path d="M3 3 L14 15 L3 27" fill="none" stroke="var(--blue)" stroke-width="4"/></svg>
    <div class="abs caption">
      <p>Lorem Ipsum is simply dummy text of the printing and typesetting industry. Lorem Ipsum has been the industry's standard</p>
      <div class="btn-appt">Make An Appointment</div>
    </div>
  </section>

  <section class="abs welcome">
    <h2>Welcome to Lumina Eye Care</h2>
    <p class="text">Lorem Ipsum is simply dummy text of the printing and typesetting industry. Lorem Ipsum has been the industry's standard dummy text ever since the 1500s, when an unknown printer took a galley of type and scrambled it to make a type specimen book. It has survived not only five centuries, but also the leap into electronic typesetting, remaining essentially unchanged.</p>
    <p class="text">Lorem Ipsum is simply dummy text of the printing and typesetting industry. Lorem Ipsum has been the industry's standard dummy text ever since the 1500s, when an unknown printer took a galley of type and scrambled it to make a type specimen book. It has survived not only five centuries, but also the leap into electronic typesetting, remaining essentially unchanged. Lorem Ipsum is simply dummy text of the printing and typesetting industry. Lorem Ipsum has been the industry's standard dummy text ever since the 1500s, when an unknown printer took a galley of type and scrambled it to make a type specimen book.</p>
  </section>

  <aside class="abs services">
    <h3>Our Services</h3>
    <ul>
      <li><svg width="6" height="8" viewBox="0 0 6 8"><path d="M1 1l3 3-3 3" fill="none" stroke="#fff" stroke-width="1.5"/></svg>Primary Vision Care</li>
      <li><svg width="6" height="8" viewBox="0 0 6 8"><path d="M1 1l3 3-3 3" fill="none" stroke="#fff" stroke-width="1.5"/></svg>Contact Lens</li>
      <li><svg width="6" height="8" viewBox="0 0 6 8"><path d="M1 1l3 3-3 3" fill="none" stroke="#fff" stroke-width="1.5"/></svg>Kids Contact Lens Clinic</li>
      <li><svg width="6" height="8" viewBox="0 0 6 8"><path d="M1 1l3 3-3 3" fill="none" stroke="#fff" stroke-width="1.5"/></svg>Eyewear Gallery</li>
      <li><svg width="6" height="8" viewBox="0 0 6 8"><path d="M1 1l3 3-3 3" fill="none" stroke="#fff" stroke-width="1.5"/></svg>Pediatrics</li>
      <li><svg width="6" height="8" viewBox="0 0 6 8"><path d="M1 1l3 3-3 3" fill="none" stroke="#fff" stroke-width="1.5"/></svg>Binocular Vision</li>
    </ul>
  </aside>

  <section class="abs col news">
    <h2>Latest News</h2>
    <div class="post"><div class="date">June 1<br>2015</div><div class="post-title">Lorem Ipsum is simply dummy text of the printing and typesetting industry.</div></div>
    <p class="text post-body">Lorem Ipsum has been the industry's standard dummy text ever since the 1500s, when an unknown printer took a galley of type and scrambled it to make a type specimen book.</p>
    <div class="divider"></div>
    <div class="post"><div class="date">June 1<br>2015</div><div class="post-title">Lorem Ipsum is simply dummy text of the printing and typesetting industry.</div></div>
    <p class="text post-body">Lorem Ipsum has been the industry's standard dummy text ever since the 1500s, when an unknown printer took a galley of type and scrambled it to make a type specimen book.</p>
  </section>

  <section class="abs col about">
    <h2>About Practise</h2>
    <div class="about-photo" role="img" aria-label="Photo of a smiling optometrist working at a laptop"></div>
    <p class="text">Lorem Ipsum is simply dummy text of the printing and typesetting industry. Lorem Ipsum has been the industry's standard dummy text ever since the 1500s, when an unknown printer took a galley of type and scrambled it to make a type specimen book. It has survived not only five centuries, but also the leap into electronic typesetting, remaining essentially unchanged. typesetting industry.</p>
  </section>

  <aside class="abs appt">
    <h3>Make an<br>Appointment</h3>
    <div class="field">Name</div>
    <div class="field">E-Mail</div>
    <div class="field">Phone</div>
    <div class="field msg">Message</div>
    <div class="submit" style="margin-top:15px">Submit</div>
  </aside>
</div>

<nav class="abs footer-nav">
  <span>Home</span><span>|</span><span>About Practise</span><span>|</span><span>Services</span><span>|</span><span>Insurance</span><span>|</span><span>Appointment</span><span>|</span><span>Our family</span><span>|</span><span>Contact Us</span>
</nav>
<p class="abs copy">© 2015 Company Name . All Rights Reserved</p>
<div class="abs social"><span></span><span></span></div>
</body>
</html>
```